BANNER FOR ONLINE CABINET COMPANY MAIN PAGE

Need 3 different banners for the main page. We are online platform for ordering cabinets, parts etc. online.
Website: trimfit.ca
A place where the banner will be placed: https://view.snapvault.example/qR7TpWzKmB4eX
Banner size: 1344x399 pixels
****Clients should get the main point that they can order everything online through the website.

Industry/Entity Type

online cabinets and parts ordering

Requirements
Must have
• online ordering icons, iphone, laptop, desktop pc - so clients get an idea that this is web based service to order cabinets

```html
<!DOCTYPE html>
<html lang="en">
<head>
<meta charset="utf-8">
<title>TrimFit homepage banners</title>
<link href="https://fonts.googleapis.com/css2?family=Roboto:wght@300;400&family=Roboto+Condensed:wght@700&family=Archivo+Black&display=swap" rel="stylesheet">
<style>
  :root{
    --stage:#383b3f;
    --slate:#595b60;
    --white:#ffffff;
    --accent-red:#e2452f;
    --pink:#f2a3a4;
    --pink-line:#e7a0a4;
    --blue:#2fa2c4;
    --blue-line:#169ed0;
    --lilac:#a8aecb;
    --lilac-line:#b8bdd6;
  }
  *{margin:0;padding:0;box-sizing:border-box}
  html,body{width:1164px;height:1200px;overflow:hidden;background:var(--stage)}
  .stage{position:relative;width:1164px;height:1200px}
  .icon-defs{position:absolute;width:0;height:0}
  .banner{position:absolute;width:1033px;height:306px;overflow:hidden}
  .banner--kitchen{left:67px;top:115px}
  .banner--storage{left:64px;top:444px}
  .banner--cabinets{left:64px;top:779px}
  .banner__art{position:absolute;inset:0;width:100%;height:100%}
  .brand{position:absolute;left:55px;top:52px;display:flex;align-items:center;gap:8px;
    font-family:"Roboto Condensed",sans-serif;font-weight:700;font-size:37px;color:var(--white);line-height:1}
  .brand__dot{width:16px;height:16px;border-radius:50%;background:var(--accent-red)}
  .offer-list{position:absolute;left:51px;top:115px;list-style:none;
    font-family:"Roboto",sans-serif;font-weight:300;font-size:26px;color:var(--white);line-height:42px;letter-spacing:.3px;white-space:nowrap}
  .device-row{position:absolute;left:452px;top:228px;display:flex;align-items:flex-end;gap:16px;opacity:.9}
  .device{display:block;fill:none;stroke:var(--white);stroke-width:2;stroke-linecap:round;stroke-linejoin:round}
  .device--phone{width:20px;height:34px}
  .device--laptop{width:50px;height:32px}
  .device--desktop{width:44px;height:40px}
  .cta{position:absolute;left:781px;top:231px;width:137px;height:25px;border-radius:13px;background:var(--white);
    font-family:"Archivo Black",sans-serif;font-size:13px;letter-spacing:.8px;color:#2f3236;
    display:flex;align-items:center;justify-content:center}
  .site-url{position:absolute;left:779px;top:268px;width:141px;text-align:center;
    font-family:"Roboto",sans-serif;font-weight:400;font-size:14px;color:var(--white)}
</style>
</head>
<body>
<svg class="icon-defs" aria-hidden="true">
  <defs>
    <symbol id="icon-phone" viewBox="0 0 20 34"><rect x="2" y="1" width="16" height="32" rx="3"/><line x1="8" y1="28.5" x2="12" y2="28.5"/></symbol>
    <symbol id="icon-laptop" viewBox="0 0 50 32"><rect x="8" y="2" width="34" height="22" rx="2"/><path d="M2 28h46l-3 3H5z"/></symbol>
    <symbol id="icon-desktop" viewBox="0 0 44 40"><rect x="2" y="2" width="40" height="27" rx="2"/><path d="M18 29v6M26 29v6M13 38h18"/></symbol>
  </defs>
</svg>
<div class="stage">

  <!-- Banner 1 -->
  <section class="banner banner--kitchen">
    <svg class="banner__art" viewBox="0 0 1344 399" preserveAspectRatio="none">
      <rect width="1344" height="399" fill="var(--pink)" role="img" aria-label="Pink-toned kitchen interior with range hood and counter"/>
      <polygon points="0,271 0,399 138,399" fill="var(--slate)"/>
      <polygon points="1000,0 1310,0 1155,155" fill="#d8c6b0" role="img" aria-label="Open kitchen shelving with jars"/>
      <polygon points="943,30 1103,190 943,350 785,190" fill="#e9e6e2" role="img" aria-label="White tiled wall with hanging utensils"/>
      <polygon points="1160,168 1344,0 1344,330 1290,399 1240,399 1160,320" fill="#dcdcdc" role="img" aria-label="Pan with kitchen utensils"/>
      <polyline points="785,190 943,30 1000,0" fill="none" stroke="var(--pink-line)" stroke-width="5"/>
      <polyline points="1155,155 1344,0" fill="none" stroke="var(--pink-line)" stroke-width="5"/>
      <polygon points="1103,191 943,399 1318,399" fill="var(--slate)"/>
      <circle cx="737" cy="63" r="3.5" fill="var(--accent-red)"/>
      <circle cx="761" cy="105" r="7.5" fill="none" stroke="#333" stroke-width="1.5"/>
      <g fill="#333">
        <circle cx="793" cy="301" r="1.6"/><circle cx="810" cy="301" r="1.6"/><circle cx="827" cy="301" r="1.6"/><circle cx="844" cy="301" r="1.6"/><circle cx="861" cy="301" r="1.6"/><circle cx="878" cy="301" r="1.6"/><circle cx="895" cy="301" r="1.6"/><circle cx="912" cy="301" r="1.6"/>
        <circle cx="793" cy="318" r="1.6"/><circle cx="810" cy="318" r="1.6"/><circle cx="827" cy="318" r="1.6"/><circle cx="844" cy="318" r="1.6"/><circle cx="861" cy="318" r="1.6"/><circle cx="878" cy="318" r="1.6"/><circle cx="895" cy="318" r="1.6"/><circle cx="912" cy="318" r="1.6"/>
        <circle cx="793" cy="342" r="1.6"/><circle cx="810" cy="342" r="1.6"/><circle cx="827" cy="342" r="1.6"/><circle cx="844" cy="342" r="1.6"/><circle cx="861" cy="342" r="1.6"/><circle cx="878" cy="342" r="1.6"/><circle cx="895" cy="342" r="1.6"/><circle cx="912" cy="342" r="1.6"/>
        <circle cx="793" cy="364" r="1.6"/><circle cx="810" cy="364" r="1.6"/><circle cx="827" cy="364" r="1.6"/><circle cx="844" cy="364" r="1.6"/><circle cx="861" cy="364" r="1.6"/><circle cx="878" cy="364" r="1.6"/><circle cx="895" cy="364" r="1.6"/><circle cx="912" cy="364" r="1.6"/>
      </g>
    </svg>
    <div class="brand">TrimFit<span class="brand__dot"></span></div>
    <ul class="offer-list">
      <li>DECORATIVE HARDWARE</li>
      <li>KITCHEN ACCESSORIES</li>
      <li>VANITIES</li>
    </ul>
    <div class="device-row" role="img" aria-label="Order from phone, laptop or desktop">
      <svg class="device device--phone"><use href="#icon-phone"/></svg>
      <svg class="device device--laptop"><use href="#icon-laptop"/></svg>
      <svg class="device device--desktop"><use href="#icon-desktop"/></svg>
    </div>
    <div class="cta">ORDER NOW</div>
    <div class="site-url">www.trimfit.ca</div>
  </section>

  <!-- Banner 2 -->
  <section class="banner banner--storage">
    <svg class="banner__art" viewBox="0 0 1344 399" preserveAspectRatio="none">
      <rect width="1344" height="399" fill="var(--blue)" role="img" aria-label="Blue-toned living room with media unit and chairs"/>
      <polygon points="0,271 0,399 138,399" fill="var(--slate)"/>
      <polygon points="1035,0 1300,0 1310,60 1155,195 1005,60" fill="#e3c8a8" role="img" aria-label="Wooden kitchen cabinetry with pendant lights"/>
      <polygon points="943,30 1103,190 943,350 785,190" fill="#ece4f1" role="img" aria-label="White floating shelves with colourful stationery"/>
      <polygon points="1160,220 1344,55 1344,399 1310,399 1160,250" fill="#e6e7e8" role="img" aria-label="White drawer unit with open drawer"/>
      <polyline points="785,190 943,30 1005,60" fill="none" stroke="var(--blue-line)" stroke-width="5"/>
      <polyline points="1155,215 1344,45" fill="none" stroke="var(--blue-line)" stroke-width="5"/>
      <polygon points="1300,0 1344,0 1344,45 1310,75" fill="var(--blue-line)"/>
      <polygon points="1103,191 943,399 1318,399" fill="var(--slate)"/>
      <polyline points="1103,191 1318,399" fill="none" stroke="var(--blue-line)" stroke-width="5"/>
      <circle cx="737" cy="63" r="3.5" fill="var(--accent-red)"/>
      <circle cx="761" cy="105" r="7.5" fill="none" stroke="#333" stroke-width="1.5"/>
      <g fill="#333">
        <circle cx="793" cy="301" r="1.6"/><circle cx="810" cy="301" r="1.6"/><circle cx="827" cy="301" r="1.6"/><circle cx="844" cy="301" r="1.6"/><circle cx="861" cy="301" r="1.6"/><circle cx="878" cy="301" r="1.6"/><circle cx="895" cy="301" r="1.6"/><circle cx="912" cy="301" r="1.6"/>
        <circle cx="793" cy="342" r="1.6"/><circle cx="810" cy="342" r="1.6"/><circle cx="827" cy="342" r="1.6"/><circle cx="844" cy="342" r="1.6"/><circle cx="861" cy="342" r="1.6"/><circle cx="878" cy="342" r="1.6"/><circle cx="895" cy="342" r="1.6"/><circle cx="912" cy="342" r="1.6"/>
        <circle cx="793" cy="364" r="1.6"/><circle cx="810" cy="364" r="1.6"/><circle cx="827" cy="364" r="1.6"/><circle cx="844" cy="364" r="1.6"/><circle cx="861" cy="364" r="1.6"/><circle cx="878" cy="364" r="1.6"/><circle cx="895" cy="364" r="1.6"/><circle cx="912" cy="364" r="1.6"/>
      </g>
    </svg>
    <div class="brand">TrimFit<span class="brand__dot"></span></div>
    <ul class="offer-list">
      <li>DRAWERS &amp; ROTS</li>
      <li>FLOATING SHELVES</li>
      <li>MELAMINE SHELVES</li>
    </ul>
    <div class="device-row" role="img" aria-label="Order from phone, laptop or desktop">
      <svg class="device device--phone"><use href="#icon-phone"/></svg>
      <svg class="device device--laptop"><use href="#icon-laptop"/></svg>
      <svg class="device device--desktop"><use href="#icon-desktop"/></svg>
    </div>
    <div class="cta">ORDER NOW</div>
    <div class="site-url">www.trimfit.ca</div>
  </section>

  <!-- Banner 3 -->
  <section class="banner banner--cabinets">
    <svg class="banner__art" viewBox="0 0 1344 399" preserveAspectRatio="none">
      <rect width="1344" height="399" fill="var(--lilac)" role="img" aria-label="Lilac-toned room with dresser, books and plants"/>
      <polygon points="0,271 0,399 138,399" fill="var(--slate)"/>
      <polygon points="1030,0 1290,0 1310,25 1155,190 995,60" fill="#d9d4cc" role="img" aria-label="Bright kitchen with white cabinets and pendant lights"/>
      <polygon points="943,30 1103,190 943,350 785,190" fill="#dedad3" role="img" aria-label="White kitchen with stainless range hood"/>
      <polygon points="1160,215 1310,68 1344,100 1344,399 1310,399 1160,250" fill="#e2e3e6" role="img" aria-label="White dresser with plants and clock"/>
      <polyline points="785,190 943,30 995,60" fill="none" stroke="var(--lilac-line)" stroke-width="5"/>
      <polygon points="1103,191 943,399 1318,399" fill="var(--slate)"/>
      <circle cx="737" cy="63" r="3.5" fill="var(--accent-red)"/>
      <circle cx="761" cy="105" r="7.5" fill="none" stroke="#333" stroke-width="1.5"/>
      <g fill="#333">
        <circle cx="793" cy="301" r="1.6"/><circle cx="810" cy="301" r="1.6"/><circle cx="827" cy="301" r="1.6"/><circle cx="844" cy="301" r="1.6"/><circle cx="861" cy="301" r="1.6"/><circle cx="878" cy="301" r="1.6"/><circle cx="895" cy="301" r="1.6"/><circle cx="912" cy="301" r="1.6"/>
        <circle cx="793" cy="318" r="1.6"/><circle cx="810" cy="318" r="1.6"/><circle cx="827" cy="318" r="1.6"/><circle cx="844" cy="318" r="1.6"/><circle cx="861" cy="318" r="1.6"/><circle cx="878" cy="318" r="1.6"/><circle cx="895" cy="318" r="1.6"/><circle cx="912" cy="318" r="1.6"/>
        <circle cx="793" cy="342" r="1.6"/><circle cx="810" cy="342" r="1.6"/><circle cx="827" cy="342" r="1.6"/><circle cx="844" cy="342" r="1.6"/><circle cx="861" cy="342" r="1.6"/><circle cx="878" cy="342" r="1.6"/><circle cx="895" cy="342" r="1.6"/><circle cx="912" cy="342" r="1.6"/>
        <circle cx="793" cy="364" r="1.6"/><circle cx="810" cy="364" r="1.6"/><circle cx="827" cy="364" r="1.6"/><circle cx="844" cy="364" r="1.6"/><circle cx="861" cy="364" r="1.6"/><circle cx="878" cy="364" r="1.6"/><circle cx="895" cy="364" r="1.6"/><circle cx="912" cy="364" r="1.6"/>
      </g>
    </svg>
    <div class="brand">TrimFit<span class="brand__dot"></span></div>
    <ul class="offer-list">
      <li>CABINET DOORS</li>
      <li>CABINETS</li>
      <li>PARTS</li>
    </ul>
    <div class="device-row" role="img" aria-label="Order from phone, laptop or desktop">
      <svg class="device device--phone"><use href="#icon-phone"/></svg>
      <svg class="device device--laptop"><use href="#icon-laptop"/></svg>
      <svg class="device device--desktop"><use href="#icon-desktop"/></svg>
    </div>
    <div class="cta">ORDER NOW</div>
    <div class="site-url">www.trimfit.ca</div>
  </section>

</div>
</body>
</html>
```